"Trelvix" printing shop

-The design must be based around the attached HPID (home page information design) called "Trelvix - HPID".

The table boxes are just for approximate placement of information – you DON'T have to box everything in and you can arrange these. All fonts used in the HPID are only examples - you can use any Zarvel font you wish.

- Information only is in orange text. Copy to go on the design in black text. Some instructions are in the HPID. Please be creative!

-The design needs to be modern. Colours are to be consistent with their new logo or complement it. Keep it clean and simple, you don't need to use lots of colours. Use lots of white.

- images / icons for the site need to be relevant and high quality, but they must also be free images or icons. I have attached a few examples that could be used.

Width of content will be 1100 pixels when implemented as a web page. Header height (without nav bar) 150-200 pixels.

If your design is chosen the winning PSD file will have to be provided as follows…
1. Canvas size of 2000px x 2000px - 72ppi in Adobe Photoshop (CS5 compatible)
2. Width of content section is 1100px wide - centered in the canvas
3. Any button rollovers/hovers in the PSD as hidden layers.
4. All fonts used must be Zarvel fonts.
5. You will need to supply the chosen home page plus one example page (example page as a style guide for how all other pages will look). Example page is only the header and navigational bar at the top, an empty sector in the middle with a column (190 px wide) which can be left or right aligned which means the main sector is 910 pixels wide, and then the footer at the bottom of the page

Checklist - http://plumvoratelist.example/

Examples of some websites that have great design... don't copy them please but they are similar in look to what we are after....
http://www.brindolfa.example/

• Drop shadows, comic sans font

```html
<!DOCTYPE html>
<html lang="en">
<head>
<meta charset="utf-8">
<title>Trelvix – Digital Printing, Laminating and Photocopying</title>
<link href="https://fonts.googleapis.com/css2?family=Open+Sans:wght@400;600;700&family=Oswald:wght@400;500&display=swap" rel="stylesheet">
<style>
:root{
  --page:#eef0f1;
  --ink:#1c1c1c;
  --muted:#555;
  --nav:#2b3e50;
  --nav-dark:#2b2b2b;
  --bar:#222;
  --accent:#e67e22;
  --teal:#1a9e80;
  --red:#c0392b;
  --blue:#1a9ad6;
  --pink:#e4007c;
  --scarlet:#e42421;
  --rust:#cf5a10;
  --yellow:#f2c300;
  --purple:#8e44ad;
  --field:#f3f4f5;
  --line:#d8dadc;
}
*{box-sizing:border-box;margin:0;padding:0}
html,body{width:1000px;height:1200px;overflow:hidden}
body{background:var(--page);font-family:"Open Sans",Arial,sans-serif;color:var(--ink);position:relative}

/* header */
.site-header{position:absolute;top:0;left:0;width:1000px;height:75px;background:var(--page)}
.brand{position:absolute;left:228px;top:12px;display:flex;align-items:center;gap:8px}
.brand-mark{width:26px;height:26px;background:var(--teal)}
.brand-name{font-size:28px;font-weight:700;color:var(--ink);line-height:1}
.brand-lines{position:absolute;left:228px;top:50px}
.motto{font-size:7.5px;font-weight:700;color:var(--ink);letter-spacing:.2px}
.tagline{font-size:6.2px;font-style:italic;color:var(--muted);margin-top:2px}
.contact{position:absolute;left:572px;top:16px;font-size:10.5px;color:var(--ink)}
.contact li{list-style:none;display:flex;align-items:center;gap:8px;height:19px}
.contact svg{width:14px;height:14px}

/* nav */
.main-nav{position:absolute;top:75px;left:0;width:1000px;height:50px;background:var(--nav)}
.footer-nav{position:absolute;top:1123px;left:0;width:1000px;height:51px;background:var(--nav-dark)}
.nav-list{position:absolute;left:234px;top:0;width:560px;display:flex;flex-wrap:wrap;list-style:none}
.nav-list li{font-size:8.4px;color:#fff;height:25px;line-height:25px;margin-right:17px;text-transform:uppercase}
.nav-list li.active{color:var(--accent)}

/* hero */
.hero{position:absolute;top:125px;left:0;width:1000px;height:271px;background:linear-gradient(115deg,#6b5a4a 0%,#8a7866 35%,#5b4d41 55%,#2a2a2a 75%,#1a1a1a 100%)}
.hero-photo{position:absolute;inset:0}
.hero-title{position:absolute;left:226px;top:86px;font-family:"Oswald",Arial,sans-serif;font-size:29px;font-weight:500;color:#fff;line-height:36px;text-transform:uppercase}
.hero-dots{position:absolute;left:493px;top:241px;display:flex;gap:6px}
.hero-dots span{width:13px;height:13px;border-radius:50%;background:#2b2b2b}
.hero-dots span.on{background:var(--teal)}
.hero-edge{position:absolute;left:0;bottom:0;width:1000px;height:2px;border-bottom:2px dotted #fff}

/* services */
.services{position:absolute;top:396px;left:0;width:1000px;height:266px}
.service{position:absolute;width:200px;text-align:center}
.tile{width:68px;height:68px;border-radius:4px;margin:0 auto;position:relative}
.tile-label{position:absolute;left:6px;top:2px;font-size:14px;color:#222}
.tile svg{position:absolute;left:16px;top:24px;width:36px;height:36px}
.service h3{font-size:12.5px;font-weight:700;margin-top:10px;text-transform:uppercase;letter-spacing:.2px}

/* features */
.features{position:absolute;top:662px;left:0;width:1000px;height:250px;background:radial-gradient(ellipse at 45% 40%,#6a6a6a 0%,#4a4a4a 45%,#333 100%)}
.swatch-photo{position:absolute;inset:0}
.feature{position:absolute;width:170px;text-align:center;color:#fff}
.feature h4{font-size:12.5px;font-weight:400;margin-bottom:7px}
.feature p{font-size:6.6px;line-height:9.5px;margin-bottom:11px}
.btn{display:inline-block;font-size:7.4px;font-weight:700;color:#fff;background:var(--accent);padding:0 10px;height:20px;line-height:20px;border-radius:2px}
.btn.red{background:var(--red)}

/* quote */
.quote{position:absolute;top:912px;left:0;width:1000px;height:211px}
.quote h2{position:absolute;left:226px;top:24px;font-size:15px;font-weight:700;letter-spacing:.3px}
.quote-intro{position:absolute;left:226px;top:56px;width:180px;font-size:7.2px;line-height:11px;color:#333}
.quote-intro p{margin-bottom:8px}
.field{position:absolute;background:var(--field);border:1px solid var(--line);font-size:7.2px;color:#555;padding:7px 9px}
.field.focus{border-color:var(--accent)}
.send{position:absolute;left:427px;top:160px;width:65px;height:24px;background:var(--teal);color:#fff;font-size:8.4px;font-weight:700;display:flex;align-items:center;justify-content:center;gap:5px;border-radius:2px}

/* bottom */
.bottom-bar{position:absolute;top:1174px;left:0;width:1000px;height:26px;background:var(--bar)}
.copyright{position:absolute;left:228px;top:8px;font-size:7.2px;color:#ccc}
.social{position:absolute;left:720px;top:8px;display:flex;gap:8px}
.social span{width:8px;height:8px;border-radius:50%;background:var(--teal)}
</style>
</head>
<body>

<header class="site-header">
  <div class="brand"><span class="brand-mark"></span><span class="brand-name">Trelvix</span></div>
  <div class="brand-lines">
    <div class="motto">QUALITY PRINTING MADE SIMPLE</div>
    <div class="tagline">PROFESSIONAL PHOTOCOPYING - DIGITAL &amp; FILM PROCESSING, DESIGN AND PRINTING</div>
  </div>
  <ul class="contact">
    <li><svg viewBox="0 0 14 14"><circle cx="7" cy="7" r="7" fill="#1a9e80"/><path d="M4.5 3.8l1.4-.3.8 1.8-.9.7a5 5 0 0 0 2.2 2.2l.7-.9 1.8.8-.3 1.4c-3 .3-6-2.7-5.7-5.7z" fill="#fff"/></svg>07 384 2619</li>
    <li><svg viewBox="0 0 14 14"><circle cx="7" cy="7" r="7" fill="#1a9e80"/><path d="M7 3a2.6 2.6 0 0 0-2.6 2.6C4.4 7.6 7 11 7 11s2.6-3.4 2.6-5.4A2.6 2.6 0 0 0 7 3zm0 3.6a1 1 0 1 1 0-2 1 1 0 0 1 0 2z" fill="#fff"/></svg>5/218 Harlow Road - Fenwick - Tauranga</li>
  </ul>
</header>

<nav class="main-nav">
  <ul class="nav-list">
    <li class="active">Home</li><li>About</li><li>Photocopying</li><li>Printing</li><li>Laminating</li><li>Business Cards</li><li>Typing Services</li><li>Film Processing</li>
    <li>Photo Printing</li><li>Passport Photos</li><li>Image Restoration</li><li>Printer Supplies</li><li>Free Quote</li><li>Contact</li>
  </ul>
</nav>

<section class="hero">
  <div class="hero-photo" role="img" aria-label="Open printed brochure lying on a wooden table"></div>
  <h1 class="hero-title">Digital printing, laminating and photocopying<br>services throughout Tauranga</h1>
  <div class="hero-dots"><span class="on"></span><span></span><span></span></div>
  <div class="hero-edge"></div>
</section>

<section class="services">
  <div class="service" style="left:200px;top:28px">
    <div class="tile" style="background:var(--blue)"><span class="tile-label">copy</span>
      <svg viewBox="0 0 36 36" fill="none" stroke="#111" stroke-width="2.4"><path d="M4 12l14-7 14 7-14 7z" fill="#111"/><path d="M4 19l14 7 14-7M4 25l14 7 14-7"/></svg></div>
    <h3>Photocopying</h3>
  </div>
  <div class="service" style="left:400px;top:28px">
    <div class="tile" style="background:var(--pink)"><span class="tile-label">bind</span>
      <svg viewBox="0 0 36 36" fill="none" stroke="#111" stroke-width="2.4"><rect x="5" y="6" width="26" height="27"/><path d="M10 2v7M16 2v7M22 2v7M28 2v7M10 16h16M10 21h16M10 26h16"/></svg></div>
    <h3>Laminating &amp; Binding</h3>
  </div>
  <div class="service" style="left:600px;top:28px">
    <div class="tile" style="background:var(--scarlet)"><span class="tile-label">print</span>
      <svg viewBox="0 0 36 36" fill="#111"><rect x="9" y="2" width="14" height="10" fill="#fff" stroke="#111" stroke-width="2"/><rect x="2" y="12" width="32" height="14"/><rect x="9" y="22" width="18" height="12" fill="#fff" stroke="#111" stroke-width="2"/></svg></div>
    <h3>Digital Printing</h3>
  </div>
  <div class="service" style="left:200px;top:152px">
    <div class="tile" style="background:var(--rust)"><span class="tile-label">film</span>
      <svg viewBox="0 0 36 36" fill="#111"><rect x="4" y="2" width="28" height="32"/><g fill="#cf5a10"><rect x="7" y="5" width="3" height="3"/><rect x="7" y="12" width="3" height="3"/><rect x="7" y="19" width="3" height="3"/><rect x="7" y="26" width="3" height="3"/><rect x="26" y="5" width="3" height="3"/><rect x="26" y="12" width="3" height="3"/><rect x="26" y="19" width="3" height="3"/><rect x="26" y="26" width="3" height="3"/><rect x="13" y="5" width="10" height="11"/><rect x="13" y="19" width="10" height="11"/></g></svg></div>
    <h3>Film Processing</h3>
  </div>
  <div class="service" style="left:400px;top:152px">
    <div class="tile" style="background:var(--yellow)"><span class="tile-label">card</span>
      <svg viewBox="0 0 36 36" fill="#111"><path d="M12 10V5h12v5" fill="none" stroke="#111" stroke-width="3"/><rect x="4" y="10" width="28" height="23" rx="3"/></svg></div>
    <h3>Business Cards</h3>
  </div>
  <div class="service" style="left:600px;top:152px">
    <div class="tile" style="background:var(--purple)"><span class="tile-label">photo</span>
      <svg viewBox="0 0 36 36"><rect x="3" y="4" width="30" height="28" fill="none" stroke="#111" stroke-width="2.6"/><path d="M7 28l8-10 6 7 4-4 5 7z" fill="#111"/><circle cx="24" cy="12" r="3" fill="#111"/></svg></div>
    <h3>Photo Printing</h3>
  </div>
</section>

<section class="features">
  <div class="swatch-photo" role="img" aria-label="Fanned colour swatch guide"></div>
  <div class="feature" style="left:225px;top:24px"><h4>Cost effective photocopying</h4><p>No matter the quantity of photocopies you need or the size of your copy - you can rely on us to provide a top quality service!</p><span class="btn red">Click for Photocopying</span></div>
  <div class="feature" style="left:415px;top:24px"><h4>Personal desktop publishing</h4><p>From personalised brochures, posters and birthday and special occasion cards to top quality, cheap business cards - you get it all!</p><span class="btn">Click for Desktop Publishing</span></div>
  <div class="feature" style="left:616px;top:24px"><h4>All digital format printing</h4><p>Either email us your file or bring it into the store and we can get you the print you need. All prints are to the highest quality.</p><span class="btn">Click for Digital Printing</span></div>
  <div class="feature" style="left:225px;top:136px"><h4>Film photo processing</h4><p>Bring in your film to the store and we will work with you to get the best quality print for your purpose and needs. We work with it all!</p><span class="btn">Click for Photo Film Processing</span></div>
  <div class="feature" style="left:415px;top:136px"><h4>Laminating and binding</h4><p>Create a professional image for your documents or books. Lamination and binding also keeps your documents well protected!</p><span class="btn">Click for Lamination &amp; Binding</span></div>
  <div class="feature" style="left:616px;top:136px"><h4>Quality digital photo prints</h4><p>Get your photo printed to your requirements - either from a file or from your digital camera. With a wide range of options you can get the print you want.</p><span class="btn">Click for Digital Photo Printing</span></div>
</section>

<section class="quote">
  <h2>GET A FREE QUOTE</h2>
  <div class="quote-intro">
    <p>...or talk to our team about your requirements. Please fill out the form below and we will contact you within a day.</p>
    <p>You can now upload and send us your file for a free quote!</p>
  </div>
  <div class="field focus" style="left:427px;top:27px;width:165px;height:25px">First Name</div>
  <div class="field" style="left:610px;top:27px;width:164px;height:25px">Last Name</div>
  <div class="field" style="left:427px;top:62px;width:165px;height:25px">Number</div>
  <div class="field" style="left:610px;top:62px;width:164px;height:25px">Email</div>
  <div class="field" style="left:427px;top:97px;width:347px;height:50px">Message</div>
  <div class="send">SEND <svg width="9" height="7" viewBox="0 0 9 7"><path d="M0 3.5h7M5 1l2.5 2.5L5 6" stroke="#fff" stroke-width="1.4" fill="none"/></svg></div>
</section>

<nav class="footer-nav">
  <ul class="nav-list">
    <li class="active">Home</li><li>About</li><li>Photocopying</li><li>Printing</li><li>Laminating</li><li>Business Cards</li><li>Typing Services</li><li>Film Processing</li>
    <li>Photo Printing</li><li>Passport Photos</li><li>Image Restoration</li><li>Printer Supplies</li><li>Free Quote</li><li>Contact</li>
  </ul>
</nav>

<footer class="bottom-bar">
  <div class="copyright">© 2015 Trelvix</div>
  <div class="social"><span></span><span></span><span></span><span></span></div>
</footer>

</body>
</html>
```